Business Card and Letterhead for Nurlo - modern real estate business

I need a double sided business card design for Nurlo. Please see business card brief here https://papers.trelvimo.net/sheet/q/7XrTbaLeZpMmQ2uWvd9HkCj4yNoEfsGi3lRtAz_pk/view?mode=shared

Please feel free to design the business cards however you feel best. I am happy to give some creative freedoms and then provide feedback from there.

Please then also create a letterhead to match the business card design

Colors

Designer to choose colors to be used in the design.

Requirements
Must have
• Must be a modern, elegant business card which looks very professional

```html
<!DOCTYPE html>
<html lang="en">
<head>
<meta charset="utf-8">
<title>Nurlo – Business Card and Letterhead</title>
<link href="https://fonts.googleapis.com/css2?family=Lato:wght@400;700;900&display=swap" rel="stylesheet">
<style>
  :root {
    --brand-red: #e0232b;
    --card-black: #1a1919;
    --ink: #161616;
    --paper: #ffffff;
    --backdrop: #e6e1da;
    --card-text: #f2f2f2;
    --photo-tone: linear-gradient(160deg, #8a9a86 0%, #5d6b55 45%, #2a2a2c 100%);
  }
  * { box-sizing: border-box; margin: 0; padding: 0; }
  html, body { width: 1200px; height: 900px; overflow: hidden; }
  body {
    background: var(--backdrop);
    font-family: "Lato", sans-serif;
    position: relative;
  }

  /* Letterhead */
  .letterhead {
    position: absolute; left: 132px; top: 112px;
    width: 493px; height: 698px;
    background: var(--paper);
    box-shadow: 0 4px 10px rgba(0,0,0,.25);
    overflow: hidden;
  }
  .letterhead__brand {
    position: absolute; left: 37px; top: 22px;
    font-weight: 900; font-size: 40px; letter-spacing: 2px;
    color: var(--brand-red); text-transform: uppercase; line-height: 1;
  }
  .letter {
    position: absolute; left: 47px; top: 178px; width: 401px;
    color: var(--ink); font-size: 9.4px; line-height: 12px;
  }
  .letter__greeting { font-weight: 700; margin-bottom: 17px; }
  .letter__para { text-align: justify; margin-bottom: 23px; }
  .letter__signoff { font-weight: 700; line-height: 13.2px; margin-top: 25px; }
  .letterhead__contact {
    position: absolute; left: 68px; top: 669px;
    font-size: 9.6px; color: var(--ink); word-spacing: 1px;
  }
  .letterhead__footer { position: absolute; left: 0; bottom: 0; width: 493px; height: 34px; }
  .letterhead__address {
    position: absolute; right: 11px; bottom: 7px;
    text-align: right; color: #fff; font-size: 8px; line-height: 10px;
  }

  /* Business cards */
  .card {
    position: absolute; width: 409px; height: 245px;
    background: var(--card-black);
    box-shadow: 0 4px 10px rgba(0,0,0,.3);
    overflow: hidden;
  }
  .card--front { left: 713px; top: 169px; }
  .card--back { left: 712px; top: 461px; height: 248px; }

  .card__name {
    position: absolute; left: 22px; top: 74px;
    color: var(--brand-red); font-weight: 900; font-size: 18.5px;
  }
  .card__role {
    position: absolute; left: 22px; top: 98px;
    color: var(--card-text); font-size: 11px;
  }
  .card__rule {
    position: absolute; left: 22px; top: 121px;
    width: 222px; height: 1.5px; background: var(--brand-red);
  }
  .card__photo {
    position: absolute; left: 239px; top: 50px;
    width: 144px; height: 144px; border-radius: 50%;
    border: 2px solid var(--brand-red);
    background: var(--photo-tone);
  }
  .card__address {
    position: absolute; left: 22px; top: 132px;
    color: var(--card-text); font-size: 11px; line-height: 14px;
  }
  .card__contacts {
    position: absolute; left: 22px; top: 170px; list-style: none;
    color: var(--card-text); font-size: 11px;
  }
  .card__contacts li { display: flex; align-items: center; height: 16px; }
  .card__contacts svg { width: 11px; height: 11px; margin-right: 9px; flex: none; }

  .card__brand {
    position: absolute; left: 0; right: 0; top: 76px;
    text-align: center; padding-right: 10px;
    color: var(--brand-red); font-weight: 900; font-size: 78px;
    letter-spacing: 4px; text-transform: uppercase; line-height: 1;
  }
</style>
</head>
<body>

<section class="letterhead">
  <div class="letterhead__brand">Nurlo</div>

  <article class="letter">
    <p class="letter__greeting">Dear Sir/Mam,</p>
    <p class="letter__para">Contrary to popular belief, Lorem Ipsum is not simply random text. It has roots in a piece of classical Latin literature from 45 BC, making it over 2000 years old. Edwin Harlow, a Latin professor at Marrow Hill College in Virginia, looked up one of the more obscure Latin words, consectetur, from a Lorem Ipsum passage, and going through the cites of the word in classical literature, discovered the undoubtable source.</p>
    <p class="letter__para">Lorem Ipsum comes from sections 1.10.32 and 1.10.33 of "de Finibus Bonorum et Malorum" (The Extremes of Good and Evil) by Corvinus Tal, written in 45 BC. This book is a treatise on the theory of ethics, very popular during the Renaissance. The first line of Lorem Ipsum, "Lorem ipsum dolor sit amet..", comes from a line in section 1.10.32.</p>
    <p class="letter__para">The standard chunk of Lorem Ipsum used since the 1500s is reproduced below for those interested. Sections 1.10.32 and 1.10.33 from "de Finibus Bonorum et Malorum" by Corvinus Tal are also reproduced in their exact original form, accompanied by English versions from the 1914 translation by H. Dellaway.</p>
    <p class="letter__para">The standard chunk of Lorem Ipsum used since the 1500s is reproduced below for those interested.</p>
    <p class="letter__signoff">Best Regards<br>Liam Porter<br>Licenced Real Estate Agent</p>
  </article>

  <p class="letterhead__contact">0412 386 590 &nbsp;|&nbsp; liam@nurlo.com &nbsp; | &nbsp;www.nurlo.com</p>

  <svg class="letterhead__footer" viewBox="0 0 493 34" aria-hidden="true">
    <rect x="0" y="26" width="493" height="8" fill="#161616"/>
    <polygon points="0,18 124,18 121,22 0,22" fill="#e0232b"/>
    <polygon points="125,18 253,18 250,22 121,22" fill="#161616"/>
    <polygon points="254,18 378,18 375,22 250,22" fill="#e0232b"/>
    <polygon points="382,0 493,0 493,34 364,34" fill="#161616"/>
  </svg>
  <p class="letterhead__address">PO Box 6130<br>Bellmere NSW 2640</p>
</section>

<section class="card card--front">
  <h1 class="card__name">Liam Porter</h1>
  <p class="card__role">Licenced Real Estate Agent</p>
  <div class="card__rule"></div>
  <div class="card__photo" role="img" aria-label="Portrait photo of the agent outdoors"></div>
  <p class="card__address">PO Box 6130<br>Bellmere NSW 2640</p>
  <ul class="card__contacts">
    <li>
      <svg viewBox="0 0 24 24"><path fill="#e0232b" d="M6.6 10.8a15.1 15.1 0 0 0 6.6 6.6l2.2-2.2c.3-.3.7-.4 1-.2 1.1.4 2.3.6 3.6.6.6 0 1 .4 1 1V20c0 .6-.4 1-1 1A17 17 0 0 1 3 4c0-.6.4-1 1-1h3.5c.6 0 1 .4 1 1 0 1.3.2 2.5.6 3.6.1.3 0 .7-.2 1z"/></svg>
      0412 386 590
    </li>
    <li>
      <svg viewBox="0 0 24 24"><rect x="2" y="5" width="20" height="14" fill="#e0232b"/><path d="M2 5l10 8 10-8" fill="none" stroke="#1a1919" stroke-width="1.8"/></svg>
      liam@nurlo.com
    </li>
    <li>
      <svg viewBox="0 0 24 24"><circle cx="12" cy="12" r="9.5" fill="none" stroke="#e0232b" stroke-width="2"/><path d="M2.5 12h19M12 2.5c3 3 3 16 0 19M12 2.5c-3 3-3 16 0 19" fill="none" stroke="#e0232b" stroke-width="1.5"/></svg>
      www.nurlo.com
    </li>
  </ul>
</section>

<section class="card card--back">
  <div class="card__brand">Nurlo</div>
</section>

</body>
</html>
```